Modernization of existing web site

Update existing web site to a professional look vs a home-made site. Site look and navigation should be up to today's standards and display properly on mobile devices.
Only simple HTML and CSS is to be used as this is a basic site. No content management.
Existing site is https://www.plinvaro.example

Target Market(s)

Insurance and Technology

Industry/Entity Type

Insurance and technology

Coding

Coded - Design and coding required

Number of Pages Required

5+ page

Font styles to use
Sans Serif

Colors
0054AA
0677BA
7BADD7
CADEEF
E8F1F8
0094D4
00A9DD
6FCCEA
C7EBF8
E9F6FB

Requirements
Must have
• A sleek, modern feel and also done with a button-downed industry in mind.
Nice to have
• Clean integration of the logo and name
Should not have
• Open to ideas

```html
<!DOCTYPE html>
<html lang="en">
<head>
<meta charset="utf-8">
<title>Plinvaro — Insurance &amp; Technology Services</title>
<link href="https://fonts.googleapis.com/css2?family=Roboto:wght@400;500;700;900&display=swap" rel="stylesheet">
<style>
:root{
  --navy:#1f3a93;
  --blue:#0054aa;
  --blue-mid:#0677ba;
  --blue-bright:#2a76c6;
  --blue-soft:#7badd7;
  --blue-pale:#cadeef;
  --blue-mist:#e8f1f8;
  --ink:#1b1b1b;
  --text:#333a44;
  --dark:#101a2c;
  --white:#ffffff;
}
*{box-sizing:border-box;margin:0;padding:0}
html,body{width:1200px;height:3418px;overflow:hidden}
body{font-family:"Roboto",Arial,sans-serif;color:var(--text);background:var(--white);position:relative}
.abs{position:absolute}
.btn{position:absolute;display:flex;align-items:center;justify-content:center;gap:12px;background:var(--navy);color:var(--white);border-radius:26px;font-weight:700;font-size:18px;text-decoration:none;letter-spacing:.2px}
.btn svg{width:16px;height:16px}

/* header */
.site-header{position:absolute;left:0;top:0;width:1200px;height:90px;background:var(--white);border-top:4px solid var(--blue-bright);z-index:5}
.brand{position:absolute;left:106px;top:26px;display:flex;align-items:center;gap:10px;font-size:34px;font-weight:700;color:var(--blue-bright);letter-spacing:.5px}
.brand-dot{width:30px;height:30px;border-radius:50%;background:var(--blue-bright)}
.main-nav{position:absolute;left:384px;top:36px;display:flex;gap:24px;font-size:15px;color:#222}
.main-nav a{color:inherit;text-decoration:none}
.main-nav .active{color:var(--blue-bright);font-weight:500}
.call-pill{position:absolute;left:934px;top:22px;width:157px;height:38px;border-radius:20px;background:var(--blue-bright);color:var(--white);font-weight:700;font-size:15px;display:flex;align-items:center;justify-content:center;gap:8px}

/* hero */
.hero{position:absolute;left:0;top:90px;width:1200px;height:666px;overflow:hidden}
.hero-photo{position:absolute;inset:0;background:linear-gradient(100deg,#1d3a62 0%,#3e5a78 30%,#8a7a66 55%,#c9b9a2 75%,#e3d8c8 100%)}
.hero-shade{position:absolute;inset:0;background:linear-gradient(90deg,rgba(16,36,72,.75) 0%,rgba(16,36,72,.35) 45%,rgba(0,0,0,0) 70%)}
.hero-copy{position:absolute;left:111px;top:176px;color:var(--white)}
.hero-mark{position:absolute;left:0;top:0;width:4px;height:106px;background:var(--blue-bright)}
.hero-kicker{margin-left:24px;font-size:26px;font-weight:500}
.hero-title{margin-left:22px;font-size:62px;font-weight:900;line-height:1.1;letter-spacing:1px}
.hero-lead{margin-top:30px;width:440px;font-size:16.5px;font-weight:500;line-height:1.65}
.hero-curve{position:absolute;left:0;bottom:0}

/* intro */
.intro-photo-main{position:absolute;left:89px;top:867px;width:389px;height:379px;background:linear-gradient(135deg,#5b7fa6,#a6b9cc 60%,#d4dbe2);box-shadow:0 10px 30px rgba(0,0,0,.18)}
.intro-photo-side{position:absolute;left:330px;top:1011px;width:263px;height:271px;background:linear-gradient(135deg,#e6e9ec,#b8c0c8 60%,#7d8894);border:3px solid var(--white);box-shadow:0 10px 30px rgba(0,0,0,.2)}
.intro-dots{position:absolute;left:484px;top:922px;width:26px;height:88px;background-image:radial-gradient(circle,var(--blue-bright) 1.8px,transparent 2px);background-size:8px 9px}
.intro-block{position:absolute;left:182px;top:1246px;width:86px;height:28px;background:var(--navy)}
.intro-copy{position:absolute;left:641px;top:832px;width:449px}
.section-title{font-size:30px;font-weight:700;color:var(--ink);line-height:1.27;letter-spacing:.2px}
.title-rule{width:50px;height:3px;background:var(--blue-bright);margin:10px 0 18px}
.body-text p{font-size:15px;line-height:1.72;text-align:justify;margin-bottom:8px}
.ghost-mark{position:absolute;border-radius:50%;background:var(--blue-mist);opacity:.7}

/* services */
.services{position:absolute;left:0;top:1393px;width:1200px;height:730px}
.services-title{position:absolute;left:0;top:114px;width:1200px;text-align:center;font-size:30px;font-weight:700;color:var(--ink)}
.services-rule{position:absolute;left:575px;top:160px;width:50px;height:3px;background:var(--blue-bright)}
.service-card{position:absolute;top:239px;width:176px;height:202px;background:var(--white);box-shadow:0 4px 18px rgba(30,60,110,.1);text-align:center;padding-top:31px}
.service-card.featured{top:216px;height:248px;width:206px;padding-top:40px}
.service-icon{width:97px;height:97px;border-radius:50%;background:var(--blue-pale);margin:0 auto;display:flex;align-items:center;justify-content:center}
.featured .service-icon{background:var(--blue-bright)}
.service-name{margin-top:14px;font-size:14.5px;font-weight:700;color:var(--ink);line-height:1.45}

/* about */
.about-copy{position:absolute;left:108px;top:2209px;width:490px}
.portrait-halo{position:absolute;left:617px;top:2191px;width:500px;height:500px;border-radius:50%;background:var(--blue-mist);opacity:.8}
.portrait-ring{position:absolute;left:642px;top:2211px;width:450px;height:450px;border-radius:50%;background:var(--navy)}
.portrait{position:absolute;left:644px;top:2217px;width:438px;height:438px;border-radius:50%;background:radial-gradient(circle at 50% 40%,#b59a7c 0%,#7a6650 55%,#3c3428 100%)}

/* contact */
.contact-band{position:absolute;left:0;top:2747px;width:1200px;height:617px;background:linear-gradient(160deg,#16233c,#0c1424 70%);overflow:hidden}
.contact-title{position:absolute;font-size:30px;font-weight:700;color:var(--white)}
.contact-rule{position:absolute;width:50px;height:3px;background:var(--white)}
.contact-item{position:absolute;left:110px;display:flex;align-items:center;gap:14px;color:var(--white);font-size:22px;line-height:1.35}
.contact-icon{width:46px;height:46px;border-radius:50%;border:2px solid var(--white);display:flex;align-items:center;justify-content:center;flex:none}
.contact-item.strong{font-weight:700}
.field{position:absolute;height:46px;background:var(--white);border-radius:23px;display:flex;align-items:center;gap:12px;padding-left:22px;font-size:15px;color:#333}
.field svg{width:14px;height:14px}
.field.message{height:113px;border-radius:18px;align-items:flex-start;padding-top:16px}

.site-footer{position:absolute;left:0;top:3364px;width:1200px;height:54px;background:#1f5fb0;color:var(--white);font-size:14px;display:flex;align-items:center;justify-content:center}
</style>
</head>
<body>

<header class="site-header">
  <div class="brand"><span class="brand-dot"></span>PLINVARO</div>
  <nav class="main-nav">
    <a class="active" href="#">HOME</a>
    <a href="#">OUR SERVICES</a>
    <a href="#">ABOUT US</a>
    <a href="#">CONTACT US</a>
    <a href="#">PRIVACY POLICY</a>
  </nav>
  <div class="call-pill">
    <svg width="14" height="14" viewBox="0 0 24 24" fill="#fff"><path d="M6.6 10.8a15 15 0 0 0 6.6 6.6l2.2-2.2c.3-.3.7-.4 1-.2 1.1.4 2.3.6 3.6.6.6 0 1 .4 1 1V20c0 .6-.4 1-1 1A17 17 0 0 1 3 4c0-.6.4-1 1-1h3.5c.6 0 1 .4 1 1 0 1.3.2 2.5.6 3.6.1.3 0 .7-.2 1z"/></svg>
    555-014-2763
  </div>
</header>

<section class="hero">
  <div class="hero-photo" role="img" aria-label="Photo of two colleagues smiling while working on a laptop in a bright office"></div>
  <div class="hero-shade"></div>
  <div class="hero-copy">
    <span class="hero-mark"></span>
    <div class="hero-kicker">WELCOME TO</div>
    <div class="hero-title">PLINVARO</div>
    <p class="hero-lead">We offer a number of different services for insurance, technology, and financial services firms.</p>
  </div>
  <a class="btn" href="#" style="left:111px;top:392px;width:206px;height:50px">GET STARTED
    <svg viewBox="0 0 16 16"><circle cx="8" cy="8" r="8" fill="#fff"/><path d="M6.5 4.5 10 8l-3.5 3.5" stroke="#1f3a93" stroke-width="2" fill="none"/></svg></a>
  <svg class="hero-curve" width="1200" height="200" viewBox="0 0 1200 200">
    <path d="M0 84 Q520 245 1200 72 L1200 200 L0 200Z" fill="#fff"/>
    <path d="M240 172 Q760 222 1200 64 L1200 90 Q780 238 240 176Z" fill="#2a76c6"/>
  </svg>
</section>

<section class="intro">
  <div class="intro-photo-main" role="img" aria-label="Photo of hands typing on a laptop with network graphics"></div>
  <div class="intro-dots"></div>
  <div class="intro-photo-side" role="img" aria-label="Photo of a desk with a laptop and printed charts being reviewed"></div>
  <div class="intro-block"></div>
  <div class="ghost-mark" style="left:866px;top:1100px;width:300px;height:300px;opacity:.5"></div>
  <div class="intro-copy">
    <h2 class="section-title">NAVIGATING BUSINESS AND TECHNOLOGY TO GENERATE RESULTS</h2>
    <div class="title-rule"></div>
    <div class="body-text">
      <p>At PLINVARO, we are here to assist you in realizing your vision for your business.</p>
      <p>We offer a number of different services for insurance, technology, and financial services firms.</p>
      <p>We have extensive experience in many areas of business and technology combined with a deep level of integrity in the way we do business.</p>
      <p>If you have a specific need not mentioned on our website, contact us today with your details.</p>
    </div>
  </div>
  <a class="btn" href="#" style="left:641px;top:1257px;width:204px;height:50px">LEARN MORE
    <svg viewBox="0 0 16 16"><circle cx="8" cy="8" r="8" fill="#fff"/><path d="M6.5 4.5 10 8l-3.5 3.5" stroke="#1f3a93" stroke-width="2" fill="none"/></svg></a>
</section>

<section class="services">
  <svg class="abs" style="left:0;top:0" width="1200" height="730" viewBox="0 0 1200 730">
    <defs><linearGradient id="svcBg" x1="0" y1="0" x2="0" y2="1"><stop offset="0" stop-color="#dde8f3"/><stop offset=".5" stop-color="#f1f5fa"/><stop offset="1" stop-color="#e3ecf5"/></linearGradient></defs>
    <path d="M0 110 Q600 -40 1200 110 L1200 620 Q620 800 0 620Z" fill="url(#svcBg)"/>
    <path d="M0 110 Q330 0 600 0 Q820 0 960 40 Q740 -10 600 8 Q300 30 0 130Z" fill="#2a76c6"/>
    <path d="M240 700 Q760 760 1200 620 L1200 642 Q780 770 240 704Z" fill="#2a76c6"/>
  </svg>
  <h2 class="services-title">OUR SERVICES</h2>
  <div class="services-rule"></div>

  <div class="service-card" style="left:113px">
    <div class="service-icon"><svg width="46" height="46" viewBox="0 0 24 24" fill="none" stroke="#0054aa" stroke-width="1.8"><circle cx="12" cy="10" r="6"/><path d="M9 16v4h6v-4M10 10l2 2 3-4"/></svg></div>
    <div class="service-name">Distribution Channel<br>Development</div>
  </div>
  <div class="service-card" style="left:303px">
    <div class="service-icon"><svg width="46" height="46" viewBox="0 0 24 24" fill="none" stroke="#0054aa" stroke-width="1.8"><rect x="9" y="9" width="6" height="6"/><path d="M12 2v5M12 17v5M2 12h5M17 12h5M5 5l3 3M19 5l-3 3M5 19l3-3M19 19l-3-3"/></svg></div>
    <div class="service-name">Distribution Channel<br>Development</div>
  </div>
  <div class="service-card featured" style="left:497px">
    <div class="service-icon"><svg width="50" height="50" viewBox="0 0 24 24" fill="none" stroke="#fff" stroke-width="1.8"><rect x="4" y="3" width="11" height="15" rx="1.5"/><path d="M7 7h5M7 10h5M7 13h3"/><path d="M16 12l4 1.5v3c0 2.2-1.7 3.8-4 4.5-2.3-.7-4-2.3-4-4.5v-3z" fill="#2a76c6"/><path d="M14.3 16.3l1.3 1.3 2.2-2.4"/></svg></div>
    <div class="service-name">Insurance Operations/<br>Process</div>
  </div>
  <div class="service-card" style="left:720px">
    <div class="service-icon"><svg width="46" height="46" viewBox="0 0 24 24" fill="none" stroke="#0054aa" stroke-width="1.8"><circle cx="12" cy="11" r="7"/><path d="M12 6l4.5 9h-9z" fill="#0054aa"/><path d="M12 10v2.5M12 14v.3" stroke="#fff"/></svg></div>
    <div class="service-name">Catastrophe Risk<br>Management</div>
  </div>
  <div class="service-card" style="left:910px">
    <div class="service-icon"><svg width="46" height="46" viewBox="0 0 24 24" fill="none" stroke="#0054aa" stroke-width="1.8"><circle cx="11" cy="12" r="5"/><path d="M11 3v2M11 19v2M2 12h2M18 12h2M5 6l1.5 1.5M17 6l-1.5 1.5M5 18l1.5-1.5M17 18l-1.5-1.5"/></svg></div>
    <div class="service-name">Interim Executive<br>Leadership</div>
  </div>

  <a class="btn" href="#" style="left:498px;top:515px;width:205px;height:50px">VIEW MORE
    <svg viewBox="0 0 16 16"><circle cx="8" cy="8" r="8" fill="#fff"/><path d="M6.5 4.5 10 8l-3.5 3.5" stroke="#1f3a93" stroke-width="2" fill="none"/></svg></a>
</section>

<section class="about">
  <div class="about-copy">
    <h2 class="section-title">ABOUT PLINVARO</h2>
    <div class="title-rule"></div>
    <div class="body-text">
      <p>Plinvaro was formed in late 2018 to bring over 35 years of experience in multiple industries and disciplines to our customers.</p>
      <p>Dan Merrow has led large and small organizations. With senior executive experience in business and technology, he has a distinct view of the business and technology needs of organizations.</p>
      <p>Dan has spent the last 20 years in various senior leadership positions at a leading property &amp; casualty insurance group, most recently as Chairman and President. He spent the early years of his career in high-tech manufacturing. He has also invested in several technology start-up’s. Since 2011, Dan has served as an independent director at one of the nation’s leading publicly traded financial services companies.</p>
    </div>
  </div>
  <a class="btn" href="#" style="left:108px;top:2605px;width:205px;height:51px">LEARN MORE
    <svg viewBox="0 0 16 16"><circle cx="8" cy="8" r="8" fill="#fff"/><path d="M6.5 4.5 10 8l-3.5 3.5" stroke="#1f3a93" stroke-width="2" fill="none"/></svg></a>
  <div class="portrait-halo"></div>
  <div class="portrait-ring"></div>
  <div class="portrait" role="img" aria-label="Portrait photo of the company founder in a dark suit"></div>
</section>

<svg class="abs" style="left:0;top:2740px" width="1200" height="130" viewBox="0 0 1200 130">
  <path d="M0 120 Q330 8 600 8 Q820 8 960 46 Q740 0 600 16 Q300 40 0 138Z" fill="#2a76c6"/>
</svg>

<section class="contact-band">
  <svg class="abs" style="left:0;top:0" width="1200" height="130" viewBox="0 0 1200 130">
    <path d="M0 0 L1200 0 L1200 130 Q600 -40 0 130Z" fill="#fff"/>
    <path d="M0 130 Q330 25 600 25 Q820 25 960 60 Q740 15 600 32 Q300 55 0 146Z" fill="#2a76c6"/>
  </svg>

  <h2 class="contact-title" style="left:110px;top:147px">CONTACT US</h2>
  <div class="contact-rule" style="left:110px;top:197px"></div>
  <div class="contact-item strong" style="top:236px">
    <span class="contact-icon"><svg width="18" height="18" viewBox="0 0 24 24" fill="#fff"><path d="M6.6 10.8a15 15 0 0 0 6.6 6.6l2.2-2.2c.3-.3.7-.4 1-.2 1.1.4 2.3.6 3.6.6.6 0 1 .4 1 1V20c0 .6-.4 1-1 1A17 17 0 0 1 3 4c0-.6.4-1 1-1h3.5c.6 0 1 .4 1 1 0 1.3.2 2.5.6 3.6.1.3 0 .7-.2 1z"/></svg></span>
    555-014-2763
  </div>
  <div class="contact-item" style="top:335px">
    <span class="contact-icon"><svg width="18" height="18" viewBox="0 0 24 24" fill="none" stroke="#fff" stroke-width="2"><rect x="3" y="5" width="18" height="14" rx="2"/><path d="M3 7l9 6 9-6"/></svg></span>
    info@plinvaro.example
  </div>
  <div class="contact-item" style="top:430px">
    <span class="contact-icon"><svg width="18" height="18" viewBox="0 0 24 24" fill="#fff"><path d="M12 2a7 7 0 0 0-7 7c0 5 7 13 7 13s7-8 7-13a7 7 0 0 0-7-7zm0 9.5a2.5 2.5 0 1 1 0-5 2.5 2.5 0 0 1 0 5z"/></svg></span>
    42 Harbor Ridge Ln Fairview,<br>NV 89000
  </div>

  <h2 class="contact-title" style="left:534px;top:147px">GET IN TOUCH</h2>
  <div class="contact-rule" style="left:534px;top:197px"></div>

  <div class="field" style="left:535px;top:227px;width:273px"><svg viewBox="0 0 24 24" fill="#222"><circle cx="12" cy="7" r="5"/><path d="M3 22c0-5 4-8 9-8s9 3 9 8z"/></svg>First Name</div>
  <div class="field" style="left:815px;top:227px;width:273px"><svg viewBox="0 0 24 24" fill="#222"><circle cx="12" cy="7" r="5"/><path d="M3 22c0-5 4-8 9-8s9 3 9 8z"/></svg>Last Name</div>
  <div class="field" style="left:535px;top:288px;width:273px"><svg viewBox="0 0 24 24" fill="#222"><path d="M2 5h20v14H2z"/><path d="M2 6l10 7 10-7" stroke="#fff" stroke-width="2" fill="none"/></svg>Email</div>
  <div class="field" style="left:815px;top:288px;width:273px"><svg viewBox="0 0 24 24" fill="none" stroke="#222" stroke-width="2.5"><rect x="6" y="2" width="12" height="20" rx="2"/></svg>Phone</div>
  <div class="field message" style="left:537px;top:349px;width:551px"><svg viewBox="0 0 24 24" fill="#222"><path d="M3 4h13v9H8l-4 4v-4H3z"/><path d="M18 8h3v9h-1v3l-3-3h-7v-2h8z"/></svg>How can we help you?</div>
  <a class="btn" href="#" style="left:535px;top:494px;width:190px;height:50px;font-size:15px">SUBMIT NOW
    <svg viewBox="0 0 24 24" fill="#fff"><path d="M22 2 2 10l7 3 2 8 3-5 5 4z"/></svg></a>
</section>

<footer class="site-footer">© 2022 Copyrights Plinvaro All Rights Reserved.</footer>

</body>
</html>
```